Cultured Vitals Website Design

We need a modern, elegant website for a nutritional product called "Cultured Vitals" which is based on the diets of people living in Longevity Hot Spots. In Longevity Hot Spots people live uncommonly longer and healthier lives. Most of these Hot Spots are in exotic locations around the world. I have attached several images taken from the Hot Spot in Costa Rica, along with our Logo and the text for the entire website. It is not necessary to use/include all of the text, we can add and adjust that later. For now, we need the design for the home page and template for interior pages. You do not have to use the images we provide, we can purchase additional images if needed. "Final selection should include Adobe Muse template file and all supporting graphics in editable formats (PhotoShop, Illustrator, etc)" We have posted several projects on Sketch Harbor and have accepted in every case. We look forward to seeing your design for our website. Thanks!
We like the look of these websites as an example. You have to press "Preview" (which is located on the right) to see the website.
https://www.pagemoldery.com/websites/templates/drift
https://www.pagemoldery.com/websites/templates/marlow
35-60 80% female, 20% male
Product
1 page

```html
<!DOCTYPE html>
<html lang="en">
<head>
<meta charset="utf-8">
<title>Cultured Vitals — Naturally Enhanced Superfoods</title>
<link rel="stylesheet" href="https://fonts.googleapis.com/css2?family=Comfortaa:wght@700&family=Open+Sans:wght@400;700&family=Arimo:wght@400;700&display=swap">
<style>
:root{
  --green:#5aab3c;
  --green-dark:#3f8f27;
  --green-light:#7cc55c;
  --ink:#333333;
  --text:#555555;
  --muted:#f2f2f2;
  --dark:#2f2f2f;
  --footer:#333333;
  --star:#e6b800;
  --white:#ffffff;
}
*{box-sizing:border-box;margin:0;padding:0}
html,body{width:1200px;height:3158px;overflow:hidden;background:var(--white)}
body{font-family:Arimo,Arial,sans-serif;color:var(--text);position:relative}
.abs{position:absolute}
.heading{font-family:Comfortaa,"Trebuchet MS",sans-serif;font-weight:700}
.body-copy{font-size:12px;line-height:23px;color:var(--text)}

/* header */
.site-header{position:absolute;left:0;top:0;width:1200px;height:93px;border-top:5px solid var(--green);background:var(--white);box-shadow:0 2px 6px rgba(0,0,0,.12);z-index:5}
.brand{position:absolute;left:86px;top:20px;display:flex;align-items:center;gap:10px}
.brand-dot{width:42px;height:42px;border-radius:50%;background:var(--green)}
.brand-name{font-family:Comfortaa,sans-serif;font-weight:700;font-size:27px;line-height:30px;color:var(--green);width:150px}
.main-nav{position:absolute;left:404px;top:35px;display:flex;gap:0;font-family:Arimo,Arial,sans-serif;font-size:15px;color:var(--ink)}
.main-nav a{color:var(--ink);text-decoration:none;position:absolute;white-space:nowrap}
.nav-active{width:42px;height:42px;border-radius:50%;border:2px solid var(--green);position:absolute;left:-20px;top:-12px}
.round-btn{position:absolute;top:29px;width:38px;height:38px;border-radius:50%;border:2px solid var(--green);display:flex;align-items:center;justify-content:center}
.round-btn.cart{border-color:#777}

/* hero */
.hero{position:absolute;left:0;top:93px;width:1200px;height:520px;background:linear-gradient(180deg,#6c7a76 0%,#56665a 40%,#2f4626 75%,#1f3318 100%)}
.hero-title{position:absolute;left:0;width:1200px;top:196px;text-align:center;font-size:50px;color:var(--white);letter-spacing:1px}
.hero-sub{position:absolute;left:0;width:1200px;top:266px;text-align:center;font-size:26px;color:var(--green-light)}
.slider-dots{position:absolute;left:41px;top:290px;display:flex;flex-direction:column;gap:12px}
.slider-dots span{width:9px;height:9px;border-radius:50%;background:var(--white)}
.hero-wave{position:absolute;left:0;top:480px}

/* welcome */
.section-title{position:absolute;left:0;width:1200px;text-align:center;font-size:29px;color:var(--ink)}
.section-title em{font-style:normal;color:var(--green)}
.intro{position:absolute;left:240px;width:720px;text-align:center}
.feature{position:absolute;width:290px;text-align:center}
.feature-badge{width:128px;height:128px;border-radius:50%;background:var(--green);margin:0 auto;display:flex;align-items:center;justify-content:center;border:6px solid #cfe8c3}
.feature-badge span{width:70px;height:70px;border-radius:50%;background:#444}
.feature h3{font-family:Comfortaa,sans-serif;font-weight:700;font-size:19px;color:var(--green-dark);margin-top:26px}
.feature p{margin-top:12px}

/* products */
.products{position:absolute;left:0;top:1101px;width:1200px;height:821px;background:var(--muted)}
.products-title{position:absolute;left:126px;top:30px;font-size:26px;color:var(--ink)}
.products-title em{font-style:normal;color:var(--green)}
.products-rule{position:absolute;left:86px;top:77px;width:70px;height:3px;background:var(--green)}
.arrow-btn{position:absolute;top:32px;width:26px;height:26px;border-radius:50%;border:1px solid #999;display:flex;align-items:center;justify-content:center}
.product-card{position:absolute;width:236px;height:318px;background:var(--white);box-shadow:0 1px 3px rgba(0,0,0,.1)}
.product-photo{position:absolute;left:8px;top:8px;width:220px;height:188px}
.product-name{position:absolute;left:8px;top:206px;font-size:13px;font-weight:700;color:var(--ink)}
.stars{position:absolute;right:10px;top:206px;font-size:11px;color:var(--star);letter-spacing:1px}
.product-card p{position:absolute;left:8px;top:232px;width:220px;font-size:11px;line-height:21px}
.categories{position:absolute;left:855px;top:32px;width:257px}
.categories-head{height:50px;background:#3b3b3b;color:var(--white);font-family:"Open Sans",sans-serif;font-weight:700;font-size:17px;padding:13px 18px;position:relative}
.categories-list{background:linear-gradient(180deg,var(--green-light),var(--green-dark));padding:14px 0 10px;list-style:none}
.categories-list li{font-size:12px;color:var(--white);padding:0 0 0 44px;line-height:32.5px;position:relative}
.categories-list li::before{content:"";position:absolute;left:18px;top:12px;width:9px;height:9px;border-radius:50%;background:var(--white)}
.promo{position:absolute;left:855px;top:484px;width:257px;height:293px;background:linear-gradient(180deg,#8a5a3a,#6b4028 60%,#8a2a2a)}
.promo-text{position:absolute;left:0;width:257px;text-align:center;color:var(--white);font-family:"Open Sans",sans-serif;font-weight:700}

/* success */
.success{position:absolute;left:0;top:1922px;width:1200px;height:337px;background:linear-gradient(180deg,#76b957,#5ea43f 60%,#4f9433)}
.success .section-title{color:var(--white)}
.success .intro{color:var(--white);left:230px;width:740px;line-height:26px}
.more-btn{position:absolute;left:476px;top:215px;width:248px;height:48px;border:2px solid var(--white);color:var(--white);font-size:13px;display:flex;align-items:center;justify-content:center}

/* blog */
.blog-card{position:absolute;top:2406px;width:322px;height:383px;background:var(--white);border:1px solid #e3e3e3;box-shadow:0 1px 3px rgba(0,0,0,.08)}
.blog-photo{position:absolute;left:8px;top:8px;width:304px;height:192px}
.date-badge{position:absolute;right:16px;top:176px;width:62px;height:74px;background:var(--green);color:var(--white);text-align:center;border:3px solid var(--white)}
.date-badge b{display:block;font-family:"Open Sans",sans-serif;font-size:26px;line-height:38px;margin-top:4px}
.date-badge small{font-size:11px}
.blog-title{position:absolute;left:10px;top:220px;font-family:"Open Sans",sans-serif;font-size:18px;color:var(--ink)}
.blog-card p{position:absolute;left:10px;top:262px;width:300px;font-size:11px;line-height:23px}
.read-more{position:absolute;left:10px;top:344px;font-size:11px;font-weight:700;color:var(--green);text-decoration:underline}

/* footer */
.site-footer{position:absolute;left:0;top:2842px;width:1200px;height:258px;background:var(--footer);color:#ddd}
.footer-brand{position:absolute;left:86px;top:78px;display:flex;align-items:center;gap:12px}
.footer-brand .brand-dot{width:52px;height:52px}
.footer-brand .brand-name{color:var(--white);font-size:38px;line-height:42px;width:auto}
.footer-col{position:absolute;top:46px}
.footer-col h4{font-family:"Open Sans",sans-serif;font-weight:700;font-size:14px;color:var(--white);margin-bottom:22px}
.footer-links{list-style:none;font-size:11px;line-height:23px}
.footer-links li::before{content:"▸";font-size:8px;margin-right:12px;color:#bbb}
.contact-row{display:flex;gap:12px;font-size:11px;line-height:16px;margin-bottom:13px}
.contact-row svg{flex:none}
.news-input{width:210px;height:28px;background:#252525;font-size:11px;color:#ccc;padding:7px 8px;margin-top:12px}
.subscribe{width:88px;height:28px;background:var(--green);color:var(--white);font-size:11px;display:flex;align-items:center;justify-content:center;margin-top:12px}
.bottom-bar{position:absolute;left:0;top:3100px;width:1200px;height:58px;background:var(--green);color:var(--white)}
.bottom-bar p{position:absolute;left:86px;top:21px;font-size:12px}
.socials{position:absolute;left:904px;top:12px;display:flex;gap:8px}
.socials span{width:34px;height:34px;border-radius:50%;border:2px solid var(--white)}
</style>
</head>
<body>

<header class="site-header">
  <div class="brand"><span class="brand-dot"></span><span class="brand-name">Cultured Vitals</span></div>
  <nav class="main-nav">
    <a style="left:0"><span class="nav-active"></span>Home</a>
    <a style="left:84px">Story</a>
    <a style="left:164px">Product</a>
    <a style="left:264px">Cultured Vitals</a>
    <a style="left:459px">FAQ's</a>
    <a style="left:543px">Contact Us</a>
  </nav>
  <span class="round-btn" style="left:1037px">
    <svg width="14" height="14" viewBox="0 0 14 14"><circle cx="6" cy="6" r="4" fill="none" stroke="#5aab3c" stroke-width="2"/><path d="M9 9l4 4" stroke="#5aab3c" stroke-width="2"/></svg>
  </span>
  <span class="round-btn cart" style="left:1077px">
    <svg width="14" height="14" viewBox="0 0 14 14"><path d="M1 2h2l2 7h7l1-5H4" fill="none" stroke="#555" stroke-width="1.6"/><circle cx="6" cy="12" r="1.2" fill="#555"/><circle cx="11" cy="12" r="1.2" fill="#555"/></svg>
  </span>
</header>

<section class="hero" role="img" aria-label="Forested mountain landscape of a longevity hot spot under a hazy sky">
  <div class="slider-dots"><span></span><span></span><span></span><span></span></div>
  <h1 class="hero-title heading">Cultured Vitals</h1>
  <p class="hero-sub heading">Naturally Enhanced Superfoods</p>
  <svg class="hero-wave" width="1200" height="140" viewBox="0 0 1200 140">
    <path d="M0 40 C200 120 380 120 600 70 C820 20 1000 -10 1200 60 L1200 140 L0 140 Z" fill="#9a9a9a"/>
    <path d="M0 52 C200 132 380 130 600 82 C820 34 1000 6 1200 72 L1200 140 L0 140 Z" fill="#ffffff"/>
  </svg>
</section>

<h2 class="section-title heading" style="top:656px">Welcome to <em>Cultured Vitals</em></h2>
<p class="intro body-copy" style="top:704px">Sed ut perspiciatis unde omnis iste natus error sit voluptatem accusantium doloremque laudantium, totam rem aperiam, eaque ipsa quae ab illo inventore veritatis et quasi architecto beatae vitae dicta sunt explicabo.</p>

<div class="feature" style="left:97px;top:800px">
  <div class="feature-badge"><span></span></div>
  <h3>Synthetic Free</h3>
  <p class="body-copy">Sed ut perspiciatis unde omnis iste natus error sit voluptatem accusantium doloremque laudantium, beatae vitae dicta sunt explicabo.</p>
</div>
<div class="feature" style="left:455px;top:800px">
  <div class="feature-badge"><span></span></div>
  <h3>Gluten Free</h3>
  <p class="body-copy">Sed ut perspiciatis unde omnis iste natus error sit voluptatem accusantium doloremque laudantium, beatae vitae dicta sunt explicabo.</p>
</div>
<div class="feature" style="left:813px;top:800px">
  <div class="feature-badge"><span></span></div>
  <h3>Soy Free</h3>
  <p class="body-copy">Sed ut perspiciatis unde omnis iste natus error sit voluptatem accusantium doloremque laudantium, beatae vitae dicta sunt explicabo.</p>
</div>

<section class="products">
  <h2 class="products-title heading">Our <em>Products</em></h2>
  <span class="products-rule"></span>
  <span class="arrow-btn" style="left:770px"><svg width="8" height="10" viewBox="0 0 8 10"><path d="M6 1L2 5l4 4" fill="none" stroke="#777" stroke-width="1.6"/></svg></span>
  <span class="arrow-btn" style="left:800px"><svg width="8" height="10" viewBox="0 0 8 10"><path d="M2 1l4 4-4 4" fill="none" stroke="#777" stroke-width="1.6"/></svg></span>

  <article class="product-card" style="left:86px;top:109px">
    <div class="product-photo" role="img" aria-label="Ginger root and ground spice on a wooden board" style="background:linear-gradient(135deg,#c98a3c,#8a5426)"></div>
    <h3 class="product-name">Organic Ginger Root</h3><span class="stars">★★★★☆</span>
    <p>Sed ut perspiciatis unde omnis iste natus error sit voluptatem accusantium dolore vitae dicta sunt explicabo.</p>
  </article>
  <article class="product-card" style="left:341px;top:109px">
    <div class="product-photo" role="img" aria-label="Sliced turmeric root on a wooden table" style="background:linear-gradient(135deg,#7a5a46,#d8602a)"></div>
    <h3 class="product-name">Organic Turmeric Root</h3><span class="stars">★★★★☆</span>
    <p>Sed ut perspiciatis unde omnis iste natus error sit voluptatem accusantium dolore vitae dicta sunt explicabo.</p>
  </article>
  <article class="product-card" style="left:596px;top:109px">
    <div class="product-photo" role="img" aria-label="Green apple beside a green smoothie" style="background:linear-gradient(135deg,#e6ecd8,#7fbf3a)"></div>
    <h3 class="product-name">Organic Broccoli</h3><span class="stars">★★★★☆</span>
    <p>Sed ut perspiciatis unde omnis iste natus error sit voluptatem accusantium dolore vitae dicta sunt explicabo.</p>
  </article>
  <article class="product-card" style="left:86px;top:452px">
    <div class="product-photo" role="img" aria-label="Fresh spinach leaves" style="background:linear-gradient(135deg,#3f6b2a,#6a8f46)"></div>
    <h3 class="product-name">Organic Spinach</h3><span class="stars">★★★★☆</span>
    <p>Sed ut perspiciatis unde omnis iste natus error sit voluptatem accusantium dolore vitae dicta sunt explicabo.</p>
  </article>
  <article class="product-card" style="left:341px;top:452px">
    <div class="product-photo" role="img" aria-label="Carrots and a glass of carrot juice" style="background:linear-gradient(135deg,#5a7a3a,#e0782a)"></div>
    <h3 class="product-name">Organic Carrot</h3><span class="stars">★★★★☆</span>
    <p>Sed ut perspiciatis unde omnis iste natus error sit voluptatem accusantium dolore vitae dicta sunt explicabo.</p>
  </article>
  <article class="product-card" style="left:596px;top:452px">
    <div class="product-photo" role="img" aria-label="Basket of blueberries" style="background:linear-gradient(135deg,#6a6470,#2f3f6a)"></div>
    <h3 class="product-name">Organic Blueberry</h3><span class="stars">★★★★☆</span>
    <p>Sed ut perspiciatis unde omnis iste natus error sit voluptatem accusantium dolore vitae dicta sunt explicabo.</p>
  </article>

  <aside class="categories">
    <div class="categories-head">Shop Categories
      <svg style="position:absolute;right:16px;top:18px" width="16" height="13" viewBox="0 0 16 13"><path d="M0 1h16M0 6.5h16M0 12h16" stroke="#fff" stroke-width="2"/></svg>
    </div>
    <ul class="categories-list">
      <li>Hot Spot Smoothie Recipes</li>
      <li>Okinawa Tropical Smoothie</li>
      <li>Symi Minty Green Smoothie</li>
      <li>Campodimele Tomato &amp; Herb</li>
      <li>Nicoya Avocado Smoothie</li>
      <li>Sardinia Red Grape Smoothie</li>
      <li>Loma Linda Nut &amp; Cinnamon</li>
      <li>Hunza Apricot Smoothie</li>
      <li>Bama Exotic Fruit Smoothie</li>
      <li>Savory Montacute Vichysoisse</li>
      <li>Smoothie</li>
    </ul>
  </aside>
  <div class="promo" role="img" aria-label="Fresh berries and fruit on a wooden table">
    <p class="promo-text" style="top:22px;font-size:34px">ORGANIC</p>
    <p class="promo-text" style="top:72px;font-size:20px">FRUITS &amp; VEGETABLE</p>
    <p class="promo-text" style="top:108px;font-size:32px">50% OFF</p>
  </div>
</section>

<section class="success" role="img" aria-label="Green tinted hillside landscape">
  <h2 class="section-title heading" style="top:60px">Success Stories</h2>
  <p class="intro" style="top:102px;font-size:12px">Sed ut perspiciatis unde omnis iste natus error sit voluptatem accusantium doloremque laudantium, totam rem aperiam, eaque ipsa quae ab illo inventore veritatis et quasi architecto beatae vitae dicta sunt explicabo. Nemo enim ipsam voluptatem quia voluptas sit aspernatur aut odit aut fugit, sed quia consequuntur magni dolores eos qui ratione voluptatem sequi nesciunt.</p>
  <span class="more-btn">CLICK HERE FOR MORE INFO</span>
</section>

<h2 class="section-title heading" style="top:2286px">Latest <em>Blog</em></h2>
<p class="intro body-copy" style="top:2330px">Sed ut perspiciatis unde omnis iste natus error sit voluptatem accusantium doloremque laudantium, totam rem aperiam, eaque ipsa quae ab illo inventore veritatis et quasi architecto beatae vitae dicta sunt explicabo.</p>

<article class="blog-card" style="left:86px">
  <div class="blog-photo" role="img" aria-label="Group of villagers in front of a green house" style="background:linear-gradient(180deg,#2f6a5a,#6a5a4a)"></div>
  <div class="date-badge"><b>01</b><small>June</small></div>
  <h3 class="blog-title">Contrary to Popular</h3>
  <p>Sed ut perspiciatis unde omnis iste natus error sit voluptatem accusantium doloremque laudantium, totam arch itecto beatae vitae dicta sunt explicabo.</p>
  <span class="read-more">READ MORE</span>
</article>
<article class="blog-card" style="left:438px">
  <div class="blog-photo" role="img" aria-label="Two travellers in sun hats outdoors" style="background:linear-gradient(135deg,#8a7a5a,#3f7a3a)"></div>
  <div class="date-badge"><b>01</b><small>June</small></div>
  <h3 class="blog-title">Contrary to Popular</h3>
  <p>Sed ut perspiciatis unde omnis iste natus error sit voluptatem accusantium doloremque laudantium, totam arch itecto beatae vitae dicta sunt explicabo.</p>
  <span class="read-more">READ MORE</span>
</article>
<article class="blog-card" style="left:789px">
  <div class="blog-photo" role="img" aria-label="Rural dirt road lined with trees" style="background:linear-gradient(180deg,#b8c8b8,#5a7a3a 50%,#a89070)"></div>
  <div class="date-badge"><b>01</b><small>June</small></div>
  <h3 class="blog-title">Contrary to Popular</h3>
  <p>Sed ut perspiciatis unde omnis iste natus error sit voluptatem accusantium doloremque laudantium, totam arch itecto beatae vitae dicta sunt explicabo.</p>
  <span class="read-more">READ MORE</span>
</article>

<footer class="site-footer">
  <div class="footer-brand"><span class="brand-dot"></span><span class="brand-name">Cultured Vitals</span></div>
  <div class="footer-col" style="left:438px">
    <h4>PRODUCTS &amp; SERVICES</h4>
    <ul class="footer-links">
      <li>HOME</li><li>STORY</li><li>PRODUCT</li><li>CULTURED VITALS</li><li>FAQ</li><li>CONTACT US</li>
    </ul>
  </div>
  <div class="footer-col" style="left:680px">
    <h4>GET IN CONTACT</h4>
    <div class="contact-row"><svg width="12" height="12" viewBox="0 0 12 12"><path d="M2 1h3l1 3-2 1a7 7 0 0 0 3 3l1-2 3 1v3c-6 0-9-3-9-9z" fill="#5aab3c"/></svg>(000)-121-1231 (Phone)</div>
    <div class="contact-row"><svg width="12" height="12" viewBox="0 0 12 12"><rect x="1" y="4" width="10" height="6" fill="#5aab3c"/><rect x="3" y="1" width="6" height="3" fill="#5aab3c"/></svg>(000)-121-1231 (Fax)</div>
    <div class="contact-row"><svg width="12" height="12" viewBox="0 0 12 12"><rect x="0.5" y="2" width="11" height="8" fill="#5aab3c"/><path d="M1 2.5l5 4 5-4" fill="none" stroke="#333" stroke-width="1"/></svg><span style="text-decoration:underline">hello@culturedvitals.example</span></div>
    <div class="contact-row"><svg width="12" height="14" viewBox="0 0 12 14"><path d="M6 0a5 5 0 0 1 5 5c0 4-5 9-5 9S1 9 1 5a5 5 0 0 1 5-5z" fill="#5aab3c"/><circle cx="6" cy="5" r="2" fill="#333"/></svg>#1452 lorem lipsum dummy<br>lorem lpsum</div>
  </div>
  <div class="footer-col" style="left:905px">
    <h4>NEWSLETTER</h4>
    <p style="font-size:11px;margin-top:-4px">Sign Up for Our Newsletter &amp; Promotion</p>
    <div class="news-input">Enter Your email Id :</div>
    <div class="subscribe">SUBSCRIBE!</div>
  </div>
</footer>

<div class="bottom-bar">
  <p>© Copy Rights 2016 Cultured Vitals .All Rights Reserved.</p>
  <div class="socials"><span></span><span></span><span></span><span></span><span></span></div>
</div>

</body>
</html>
```